Kestrel Calisthenics Gym Website

We need a website design for our gym.

Kestrel is the UAE's first calisthenics and parkour gym. The theme under which the gym revolves is that one does not require any machinery to workout as our bodies could be themselves the machinery. The gym is designed to be the more of a social hub rather than an "in-and-out" gym, where people come train, have fun, hang out and socialize for a few hours rather than just train for 60 minutes then leave. The gym is designed to be a big open space with lots of natural sunlight, natural wood and plants all over the place to create a natural and refreshing setting. We also use recycled material throughout the gym and recycle our waste as being green is part of our philosophy. We currently also have some of the world's top and most recognized calisthenics athletes working with us.

We would like our website to reflect all that as well as provide a simple, interactive and fun way for visitors to be able to get class and gym information, check out gym media and contact us for bookings.

Target Market(s)

Ages 15-35

Industry/Entity Type

Fitness

Coding

Coded - Design and coding required

Number of Pages Required

4 page

Font styles to use
Decorative

Colors
0792cd

Requirements
Must have
• Class descriptions
• Gym description
• Class schedules
• Trainer profiles
• Gym philosophy
• Contact Details
Nice to have
• A link to contact us directly for a free first trial class

```html
<!DOCTYPE html>
<html lang="en">
<head>
<meta charset="utf-8">
<title>Kestrel Calisthenics Gym – Class Schedules</title>
<link rel="stylesheet" href="https://fonts.googleapis.com/css2?family=Cabin:wght@400;700&family=Arimo:wght@700&display=swap">
<style>
  :root {
    --page-bg: #c6c6c6;
    --top-strip: #d3d3d3;
    --header-bg: #e0e0dc;
    --rule: #3a3a3a;
    --ink: #2a2a2a;
    --nav-active: #7a7a7a;
    --head-blue: #0b6aa5;
    --grid-line: #2f2f2f;
    --cell: #c6c6c6;
    --red: #ec1c24;
    --blue: #6a8dcd;
    --purple: #a07cc0;
    --green: #d2e68c;
    --orange: #f5a56d;
    --black: #1f1d1d;
    --icon: #555555;
  }
  * { margin: 0; padding: 0; box-sizing: border-box; }
  html, body { width: 1200px; height: 601px; overflow: hidden; }
  body {
    position: relative;
    background: var(--page-bg);
    font-family: "Cabin", sans-serif;
    color: var(--ink);
  }
  .top-strip { position: absolute; left: 0; top: 0; width: 100%; height: 22px; background: var(--top-strip); }
  .site-header {
    position: absolute; left: 0; top: 22px; width: 100%; height: 62px;
    background: var(--header-bg); border-bottom: 1px solid var(--rule);
  }
  .brand-name {
    position: absolute; left: 366px; top: 40px;
    font-size: 14px; font-weight: 400; color: var(--ink); line-height: 1; white-space: nowrap;
  }
  .main-nav { position: absolute; top: 38px; left: 579px; display: flex; gap: 13px; font-size: 11.5px; }
  .main-nav a { color: var(--ink); text-decoration: none; }
  .main-nav a.is-active { color: var(--nav-active); }

  .download-icon { position: absolute; left: 582px; top: 127px; width: 29px; height: 30px; }

  .schedule {
    position: absolute; left: 325px; top: 174px;
    display: grid;
    grid-template-columns: 62px repeat(7, 67px);
    grid-template-rows: 15px repeat(14, 15.6px);
    gap: 2px;
    padding: 2px;
    background: var(--grid-line);
    font-family: "Arimo", sans-serif; font-weight: 700;
  }
  .schedule > * {
    background: var(--cell); color: #fff;
    display: flex; align-items: center; justify-content: center;
    font-size: 7px; text-transform: uppercase; white-space: nowrap; overflow: hidden;
  }
  .schedule .col-head { background: var(--head-blue); font-size: 10px; text-transform: none; }
  .schedule .time { background: var(--head-blue); font-size: 8.5px; }
  .cls-red { background: var(--red) !important; }
  .cls-blue { background: var(--blue) !important; }
  .cls-purple { background: var(--purple) !important; }
  .cls-green { background: var(--green) !important; }
  .cls-orange { background: var(--orange) !important; }
  .rest { background: var(--black) !important; }
  .split { flex-direction: column; gap: 1px; background: var(--grid-line) !important; }
  .split > span { flex: 1; width: 100%; display: flex; align-items: center; justify-content: center; font-size: 6.5px; line-height: 1; }
  .rest-day { flex-direction: column; justify-content: space-around; font-size: 16px !important; padding: 1px 0; }

  .gym-intro {
    position: absolute; left: 284px; top: 502px; width: 630px;
    font-size: 9.9px; line-height: 11.9px; text-align: justify; color: #333;
  }
</style>
</head>
<body>
  <div class="top-strip"></div>
  <header class="site-header">
    <span class="brand-name">Kestrel Calisthenics Gym</span>
    <nav class="main-nav">
      <a href="#">Gym Info</a>
      <a href="#" class="is-active">Class Schedules</a>
      <a href="#">Trainer Profiles</a>
      <a href="#">Contact</a>
    </nav>
  </header>

  <svg class="download-icon" viewBox="0 0 29 30" aria-label="Download schedule">
    <path d="M1 7h8v3H4v16h3v-8h15v8h3V10h-5V7h8v22H1z" fill="var(--icon)"/>
    <rect x="10" y="21" width="3" height="5" fill="var(--icon)"/>
    <rect x="16" y="21" width="3" height="5" fill="var(--icon)"/>
    <path d="M13 0h3v8h4l-5.5 6L9 8h4z" fill="var(--icon)"/>
  </svg>

  <section class="schedule" aria-label="Weekly class schedule">
    <div class="col-head" style="grid-area:1/1">TIME</div>
    <div class="col-head" style="grid-area:1/2">Sunday</div>
    <div class="col-head" style="grid-area:1/3">Monday</div>
    <div class="col-head" style="grid-area:1/4">Tuesday</div>
    <div class="col-head" style="grid-area:1/5">Wednesday</div>
    <div class="col-head" style="grid-area:1/6">Thursday</div>
    <div class="col-head" style="grid-area:1/7">Friday</div>
    <div class="col-head" style="grid-area:1/8">Saturday</div>

    <div class="time" style="grid-area:2/1">6:00AM</div>
    <div class="time" style="grid-area:3/1">7:00AM</div>
    <div class="time" style="grid-area:4/1">8:00AM</div>
    <div class="time" style="grid-area:5/1">9:00AM</div>
    <div class="time" style="grid-area:6/1">10:00AM</div>
    <div class="time" style="grid-area:7/1">11:00AM</div>
    <div class="time" style="grid-area:8/1">2:00PM</div>
    <div class="time" style="grid-area:9/1">3:00PM</div>
    <div class="time" style="grid-area:10/1">4:00PM</div>
    <div class="time" style="grid-area:11/1">5:00PM</div>
    <div class="time" style="grid-area:12/1">6:00PM</div>
    <div class="time" style="grid-area:13/1">7:00PM</div>
    <div class="time" style="grid-area:14/1">8:00PM</div>
    <div class="time" style="grid-area:15/1">9:00PM</div>

    <!-- Sunday -->
    <div class="cls-red" style="grid-area:3/2">Metcon</div>
    <div class="cls-green" style="grid-area:11/2">PK Kids</div>
    <div class="cls-blue" style="grid-area:12/2">Foundation</div>
    <div class="split" style="grid-area:13/2"><span class="cls-orange">Yoga</span><span class="cls-blue">Foundation</span></div>
    <div class="cls-blue" style="grid-area:14/2">Graduate</div>
    <!-- Monday -->
    <div class="cls-purple" style="grid-area:9/3">Beginners</div>
    <div class="cls-blue" style="grid-area:10/3">Foundation</div>
    <div class="cls-purple" style="grid-area:11/3">Advanced</div>
    <div class="cls-blue" style="grid-area:12/3">Graduate</div>
    <div class="cls-red" style="grid-area:13/3"></div>
    <div class="cls-red" style="grid-area:14/3">Calisthenics</div>
    <div class="cls-red" style="grid-area:15/3"></div>
    <!-- Tuesday -->
    <div class="cls-red" style="grid-area:3/4">Metcon</div>
    <div class="cls-blue" style="grid-area:4/4">Mobility</div>
    <div class="cls-purple" style="grid-area:10/4">Beginners</div>
    <div class="cls-blue" style="grid-area:12/4">Foundation</div>
    <div class="cls-blue" style="grid-area:13/4">Dynamics</div>
    <div class="cls-blue" style="grid-area:14/4">Graduate</div>
    <!-- Wednesday -->
    <div class="cls-purple" style="grid-area:11/5">Workout</div>
    <div class="cls-orange" style="grid-area:12/5">Yoga</div>
    <div class="split" style="grid-area:13/5"><span class="cls-purple">Advanced</span><span class="cls-blue">Foundation</span></div>
    <div class="cls-blue" style="grid-area:14/5">Graduate</div>
    <!-- Thursday -->
    <div class="cls-red" style="grid-area:3/6">Metcon</div>
    <div class="split" style="grid-area:12/6"><span class="cls-purple">Beginners</span><span class="cls-blue">Mobility</span></div>
    <div class="split" style="grid-area:13/6"><span class="cls-purple">Advanced</span><span class="cls-blue">Foundation</span></div>
    <div class="cls-blue" style="grid-area:14/6">Graduate</div>
    <!-- Friday -->
    <div class="rest" style="grid-area:2/7/4/8"></div>
    <div class="cls-red" style="grid-area:4/7"></div>
    <div class="cls-red" style="grid-area:5/7">Mobility</div>
    <div class="cls-red" style="grid-area:6/7">Calisthenics</div>
    <div class="cls-red" style="grid-area:7/7"></div>
    <div class="rest rest-day" style="grid-area:8/7/16/8"><span>R</span><span>E</span><span>S</span><span>T</span><span>D</span><span>A</span><span>Y</span></div>
    <!-- Saturday -->
    <div class="cls-green" style="grid-area:9/8">PK Kids</div>
    <div class="cls-purple" style="grid-area:11/8">Open Session</div>
    <div class="cls-blue" style="grid-area:12/8">Leg Day</div>
    <div class="cls-blue" style="grid-area:14/8">Dynamics</div>

    <!-- open slots -->
    <span></span><span></span><span></span><span></span><span></span><span></span><span></span><span></span><span></span><span></span>
    <span></span><span></span><span></span><span></span><span></span><span></span><span></span><span></span><span></span><span></span>
    <span></span><span></span><span></span><span></span><span></span><span></span><span></span><span></span><span></span><span></span>
    <span></span><span></span><span></span><span></span><span></span><span></span><span></span><span></span><span></span><span></span>
    <span></span><span></span><span></span><span></span><span></span><span></span><span></span><span></span><span></span><span></span>
    <span></span><span></span><span></span><span></span>
  </section>

  <p class="gym-intro">Kestrel is the UAE's first calisthenics and parkour gym. The theme under which the gym revolves is that one does not require any machinery to workout as our bodies could be themselves the machinery. The gym is designed to be the more of a social hub rather than an "in-and-out" gym, where people come train, have fun, hang out and socialize for a few hours rather than just train for 60 minutes then leave. The gym is designed to be a big open space with lots of natural sunlight, natural wood and plants all over the place to create a natural and refreshing setting. We also use recycled material throughout the gym and recycle our waste as being green is part of our philosophy. We currently also have some of the world's top and most recognized calisthenics athletes working with us.</p>
</body>
</html>
```